" A empresa opera um ecossistema que conecta o transporte público a benefícios sociais, permitindo que usuários de cartões de transporte possam acessar serviços de saúde, descontos e recargas integradas por meio de um modelo digital de adesão e refiliação. "

```html
<!DOCTYPE html>
<html lang="pt-BR">
<head>
<meta charset="UTF-8">
<title>Rota Comum: Saúde e Mobilidade Unidas</title>
<link rel="stylesheet" href="https://fonts.googleapis.com/css2?family=Poppins:wght@400;600&display=swap">
<style>
  :root {
    --page-bg: #ffffff;
    --navy-deep: #0b2238;
    --navy: #12304b;
    --navy-soft: #1a3d5c;
    --teal: #4f9fb3;
    --teal-bright: #5bb0c2;
    --text-light: #ffffff;
    --photo-warm: #b9a88a;
    --photo-cool: #6f8796;
  }
  * { margin: 0; padding: 0; box-sizing: border-box; }
  html, body {
    width: 1200px;
    height: 1200px;
    overflow: hidden;
    background: var(--page-bg);
  }
  .canvas {
    position: relative;
    width: 1200px;
    height: 1200px;
    background: var(--page-bg);
    font-family: 'Poppins', sans-serif;
  }
  .feature-band {
    position: absolute;
    left: 0;
    top: 264px;
    width: 1200px;
    height: 672px;
    background: linear-gradient(100deg, var(--navy-deep) 0%, var(--navy) 45%, var(--navy-soft) 100%);
  }
  .photo-area {
    position: absolute;
    left: 72px;
    top: 336px;
    width: 451px;
    height: 528px;
    border-top-right-radius: 96px;
    background: linear-gradient(135deg, var(--photo-cool) 0%, #a7b6b8 35%, var(--photo-warm) 70%, #7d6f5a 100%);
  }
  .photo-accent {
    position: absolute;
    left: 67px;
    top: 828px;
    width: 238px;
    height: 60px;
    background: var(--teal);
  }
  .content {
    position: absolute;
    left: 557px;
    top: 400px;
    width: 520px;
  }
  .headline {
    font-weight: 600;
    font-size: 31px;
    line-height: 40px;
    letter-spacing: 1.5px;
    text-transform: uppercase;
    color: var(--text-light);
  }
  .headline .brand { color: var(--teal-bright); display: block; }
  .divider {
    width: 235px;
    height: 4px;
    background: var(--teal);
    margin: 30px 0 26px;
  }
  .lead {
    font-weight: 400;
    font-size: 27px;
    line-height: 40px;
    color: var(--text-light);
  }
  .lead .highlight { color: var(--teal-bright); }
  .footer-bar {
    position: absolute;
    left: 557px;
    top: 840px;
    width: 483px;
    height: 18px;
    background: var(--teal);
  }
</style>
</head>
<body>
<div class="canvas">
  <div class="feature-band"></div>
  <div class="photo-area" role="img" aria-label="Fotografia de passageiros sorridentes dentro de um ônibus, uma jovem em pé segurando o celular"></div>
  <div class="photo-accent"></div>
  <div class="content">
    <h1 class="headline"><span class="brand">Rota Comum:</span>Saúde e mobilidade unidas</h1>
    <div class="divider"></div>
    <p class="lead">O negócio da <span class="highlight">Rota Comum</span> é unir a experiência do usuário do <span class="highlight">Transporte Público</span> a um <span class="highlight">benefício único de saúde</span>, capaz de <span class="highlight">transformar</span> a realidade de milhares de famílias brasileiras.</p>
  </div>
  <div class="footer-bar"></div>
</div>
</body>
</html>
```